Food delivery wordpress design

need food delivery wordpress design for my site, here's the requirements
1. site must be pixel perfect , clean and professional
2. logo provided and must be match with the color scheme
3. pages : home , about us , faq , vendor registration

*** this is a information site no order can be made from the site, the site will show how things work , how to register as vendor , how to use the app , you may use any stock photo from pixelbarnhub and send me the code, i will purchase it

you may use any of the logo to play with it

***** It must look scale and not looks like template where I can purchase elsewhere
Updates

the designer told me he can't work as he got his personal problem, please check his message

Target Market(s)

those who prefer to purchase online

Font styles to use
Sans Serif

Requirements
Must have
• refer to tovimo.com/my
Nice to have
• everything user and vendor like to know

```html
<!DOCTYPE html>
<html lang="en">
<head>
<meta charset="utf-8">
<title>dapurlaju – Food delivery</title>
<link href="https://fonts.googleapis.com/css2?family=Ubuntu:wght@300;400;500&display=swap" rel="stylesheet">
<style>
:root{
  --orange:#fbb034;
  --orange-deep:#f39c1f;
  --dark:#3d3d37;
  --grey:#dddddd;
  --grey-soft:#ececec;
  --ink:#333330;
  --white:#ffffff;
}
*{margin:0;padding:0;box-sizing:border-box}
html,body{width:1200px;height:3063px;overflow:hidden}
body{position:relative;font-family:"Ubuntu",sans-serif;color:var(--ink);background:var(--white)}
.abs{position:absolute}
.band{position:absolute;left:0;width:1200px}
.hero-bg{top:0;height:560px;background:var(--orange)}
.order-bg{top:540px;height:392px;background:var(--grey)}
.vendor-bg{top:1278px;height:684px;background:var(--dark)}
.app-bg{top:2380px;height:370px;background:var(--orange)}
.footer-bg{top:2750px;height:313px;background:var(--grey)}
svg.layer{position:absolute;left:0}

.brand{font-size:25px;font-weight:500;color:var(--dark);display:flex;align-items:center;gap:8px}
.brand-dot{width:30px;height:30px;border-radius:50%;background:var(--dark)}
.nav{top:26px;left:678px;display:flex;gap:18px;font-size:12px;color:var(--dark)}
.nav .active{color:var(--white)}
.btn{position:absolute;display:flex;align-items:center;justify-content:center;font-size:11px;border-radius:2px}
.btn-dark{background:var(--dark);color:var(--orange)}
.btn-white{background:var(--white);color:var(--dark)}
.btn-orange{background:var(--orange);color:var(--dark)}

.hero-title{top:146px;left:200px;font-size:38px;line-height:45px;font-weight:400;color:var(--dark);width:420px}
.section-title{position:absolute;left:0;width:1200px;text-align:center;font-weight:400;font-size:30px;color:var(--dark)}

.step-label{position:absolute;width:150px;text-align:center;font-size:12px;line-height:15px;color:var(--dark)}
.badge{position:absolute;width:100px;height:31px;border-radius:3px;background:#2b2b28;border:1px solid #555}

.placeholder{position:absolute}
.welcome-title{top:990px;left:612px;font-size:30px;font-weight:400;color:var(--dark)}
.welcome-copy{top:1034px;left:612px;width:388px;font-size:10.5px;line-height:15px;font-weight:300;color:var(--dark)}
.welcome-copy p+p{margin-top:15px}

.vendor-title{color:var(--white)}
.vendor-intro{top:1438px;left:250px;width:700px;text-align:center;font-size:10.5px;line-height:15px;color:var(--white);font-weight:300}
.vstep{position:absolute;color:var(--white);width:260px}
.vstep h3{font-size:16px;font-weight:400;margin-bottom:8px}
.vstep p{font-size:10.5px;line-height:15px;font-weight:300}
.vstep.right-align{text-align:right}

.faq{position:absolute;left:294px;top:2038px;width:612px;border-top:1px solid #e4e4e4}
.faq-item{border-bottom:1px solid #e4e4e4;padding:0 12px;height:38px;display:flex;justify-content:space-between;align-items:center;font-size:13px;color:var(--dark)}
.faq-item .sign{font-size:18px;font-weight:300;color:#777}
.faq-item.open{background:var(--grey);height:88px;display:block;padding:10px 12px}
.faq-item.open .q{display:flex;justify-content:space-between;font-size:13px}
.faq-item.open p{margin-top:8px;font-size:10px;line-height:14px;color:#555;font-weight:300;width:560px}

.app-title{top:2548px;left:200px;font-size:36px;font-weight:400;color:var(--dark)}
.app-copy{top:2603px;left:200px;width:460px;font-size:10.5px;line-height:15px;color:#6b5a2e;font-weight:300}

.foot-col h4{font-size:14px;font-weight:400;color:var(--dark);margin-bottom:18px}
.foot-col a{display:block;font-size:10px;color:var(--dark);text-decoration:none;line-height:22.6px;font-weight:300}
.foot-col a.hl{color:var(--orange-deep)}
.contact{font-size:10px;color:var(--dark);font-weight:300}
.contact .call{font-size:15px;font-weight:400;margin-bottom:4px}
.select{top:2818px;left:818px;width:182px;height:32px;background:var(--white);display:flex;align-items:center;padding:0 12px;font-size:11px;color:var(--dark);gap:10px}
.select .flag{width:16px;height:16px;border-radius:50%;background:#c9302c}
.select .chev{margin-left:auto;color:var(--orange-deep);font-size:10px}
.social{position:absolute;top:2870px;width:24px;height:24px;border-radius:50%;background:var(--dark)}
.copyright{top:3014px;left:200px;font-size:9.5px;color:var(--dark);font-weight:300}
</style>
</head>
<body>

<!-- HERO -->
<div class="band hero-bg"></div>
<div class="band order-bg"></div>
<svg class="layer" style="top:0" width="1200" height="560" viewBox="0 0 1200 560">
  <path d="M0,548 C120,525 220,405 335,410 C455,416 560,528 700,522 C830,515 990,280 1200,425 L1200,560 L0,560Z" fill="#dddddd" stroke="#c9c9c9" stroke-width="5"/>
  <path d="M700,125 C790,95 870,150 920,205 C980,180 1070,190 1110,250 C1140,300 1110,360 1080,400 C1030,470 930,520 840,510 C760,500 700,450 670,380 C630,300 610,200 700,125Z" fill="#d99a2a" opacity=".85"/>
</svg>
<div class="placeholder" role="img" aria-label="Plated grilled steak with fresh salad, lime and spices on a marble table" style="top:146px;left:656px;width:468px;height:390px;background:linear-gradient(135deg,#f2eeee,#d7c6c8 55%,#8a5a3a);clip-path:path('M60,20 C140,-10 220,40 270,80 C330,45 430,55 455,120 C475,185 440,250 400,300 C350,360 250,400 170,385 C95,370 40,320 20,250 C-5,170 -5,60 60,20Z')"></div>

<div class="abs brand" style="top:12px;left:200px"><span class="brand-dot"></span>dapurlaju</div>
<nav class="abs nav"><span class="active">- Home -</span><span>About Us</span><span>FAQ</span></nav>
<div class="btn btn-dark" style="top:15px;left:862px;width:138px;height:31px">Vendor Registration</div>

<h1 class="abs hero-title">Despite these uncertain times, we're still here to serve you</h1>
<div class="btn btn-white" style="top:302px;left:200px;width:107px;height:32px">Get Started</div>

<!-- HOW TO ORDER -->
<h2 class="section-title" style="top:598px">How to order from our app</h2>
<svg class="layer" style="top:640px" width="1200" height="120" viewBox="0 640 1200 120">
  <g fill="none" stroke="#e0902a" stroke-width="1.4" stroke-dasharray="4 3">
    <path d="M203,661 Q230,685 250,690"/>
    <path d="M312,700 Q360,725 406,724"/>
    <path d="M474,722 Q520,705 566,694"/>
    <path d="M634,696 Q690,712 726,722"/>
    <path d="M794,720 Q850,712 886,697"/>
    <path d="M952,686 Q975,670 996,661"/>
    <circle cx="281" cy="692" r="34"/>
    <circle cx="440" cy="724" r="34"/>
    <circle cx="600" cy="692" r="34"/>
    <circle cx="760" cy="724" r="34"/>
    <circle cx="919" cy="692" r="34"/>
  </g>
  <circle cx="203" cy="661" r="3" fill="#e0902a"/>
  <circle cx="996" cy="661" r="3" fill="#e0902a"/>
  <g fill="none" stroke="#3d3d37" stroke-width="2.2" stroke-linecap="round" stroke-linejoin="round">
    <path d="M266,688 Q281,672 296,688Z M266,694 H296 M266,700 H296 Q296,706 290,706 H272 Q266,706 266,700"/>
    <path d="M440,740 C430,726 428,718 428,714 A12,12 0 1 1 452,714 C452,718 450,726 440,740Z"/><circle cx="440" cy="714" r="4"/>
    <path d="M590,676 V708 M586,676 V688 Q590,692 594,688 V676 M608,676 Q600,684 604,692 H608 V708 M608,676 V692"/>
    <path d="M745,718 H775 L770,736 H750Z M750,718 L760,708 L770,718 M755,723 V731 M760,723 V731 M765,723 V731"/>
    <path d="M902,692 L910,700 L926,682 M914,700 L936,680"/>
  </g>
</svg>
<div class="step-label" style="top:740px;left:206px">Launch the our app<br>and select "Food"</div>
<div class="step-label" style="top:772px;left:365px">Enter your delivery<br>address.</div>
<div class="step-label" style="top:740px;left:525px">Select your favourite<br>restaurant.</div>
<div class="step-label" style="top:772px;left:685px">Select a meal and add<br>to your basket.</div>
<div class="step-label" style="top:740px;left:844px">Complete the order<br>and get ready to enjoy<br>your meal.</div>
<div class="badge" style="top:836px;left:493px"></div>
<div class="badge" style="top:836px;left:606px"></div>

<!-- WELCOME -->
<div class="placeholder" role="img" aria-label="Running chef character mascot illustration" style="top:900px;left:200px;width:378px;height:354px;background:linear-gradient(160deg,#f0efec 0 45%,#fbb034 46% 100%)"></div>
<h2 class="abs welcome-title">Welcome to dapurlaju</h2>
<div class="abs welcome-copy">
  <p>It is a long established fact that a reader will be distracted by the readable content of a page when looking at its layout. The point of using Lorem Ipsum is that it has a more-or-less normal distribution of letters, as opposed to using 'Content here, look like readable English. Many desktop publishing packages and web page editors now use lorem Ipsum.</p>
  <p>There are many variations of passages of Lorem Ipsum available, lorem but the majority have suffered alteration in some form, by injected humour, or randomised words which don't look even slightly ...</p>
</div>
<div class="btn btn-orange" style="top:1210px;left:612px;width:106px;height:30px">About Us</div>

<!-- VENDOR -->
<div class="band vendor-bg"></div>
<svg class="layer" style="top:1270px" width="1200" height="70" viewBox="0 1270 1200 70">
  <path d="M0,1270 H1200 V1278 Q600,1365 0,1278Z" fill="#ffffff"/>
  <path d="M120,1297 Q600,1360 1080,1297 Q600,1345 120,1297Z" fill="#fbb034"/>
</svg>
<svg class="layer" style="top:1890px" width="1200" height="80" viewBox="0 1890 1200 80">
  <path d="M0,1962 Q600,1870 1200,1962 V1970 H0Z" fill="#ffffff"/>
  <path d="M120,1944 Q600,1880 1080,1944 Q600,1895 120,1944Z" fill="#fbb034"/>
</svg>

<svg class="layer" style="top:1410px" width="1200" height="10" viewBox="0 1410 1200 10"><path d="M200,1414 H412 M788,1414 H1000" stroke="#8a8a84" stroke-width="1"/></svg>
<h2 class="section-title vendor-title" style="top:1392px">How to register as vendor</h2>
<div class="abs vendor-intro">It is a long established fact that a reader will be distracted by the readable content of a page when looking at its layout. The point of using Lorem Ipsum is that it has a more-or-less normal distribution of letters, as opposed to using 'Content here.</div>

<svg class="layer" style="top:1490px" width="1200" height="300" viewBox="0 1490 1200 300">
  <g stroke="#d0d0cc" stroke-width="1.4" fill="none">
    <path d="M600,1496 V1778 M543,1541 H590 M610,1635 H656 M543,1728 H590"/>
    <path d="M595,1583 L600,1589 L605,1583 M595,1677 L600,1683 L605,1677"/>
  </g>
  <circle cx="600" cy="1496" r="3" fill="#d0d0cc"/><circle cx="600" cy="1778" r="3" fill="#d0d0cc"/>
  <g fill="#d0d0cc" font-family="Ubuntu,sans-serif" font-size="9" text-anchor="middle">
    <circle cx="600" cy="1541" r="9"/><circle cx="600" cy="1635" r="9"/><circle cx="600" cy="1728" r="9"/>
    <text x="600" y="1544" fill="#3d3d37">1</text><text x="600" y="1638" fill="#3d3d37">2</text><text x="600" y="1731" fill="#3d3d37">3</text>
  </g>
</svg>
<div class="placeholder" role="img" aria-label="Clipboard and pencil illustration" style="top:1494px;left:449px;width:94px;height:94px;border-radius:50%;background:radial-gradient(circle,#fbb034 0 30%,#ececec 31%)"></div>
<div class="placeholder" role="img" aria-label="Product catalogue screen illustration" style="top:1588px;left:656px;width:94px;height:94px;border-radius:50%;background:radial-gradient(circle,#fbb034 0 30%,#ececec 31%)"></div>
<div class="placeholder" role="img" aria-label="Shopping bags with price tag illustration" style="top:1681px;left:449px;width:94px;height:94px;border-radius:50%;background:radial-gradient(circle,#e0902a 0 30%,#ececec 31%)"></div>

<div class="vstep right-align" style="top:1516px;left:176px"><h3>Submit your details</h3><p>Lorem Ipsum is simply dummy text of the<br>printing and typesetting industry.</p></div>
<div class="vstep" style="top:1608px;left:762px"><h3>Submit your catalogue</h3><p>Lorem Ipsum is simply dummy text of the<br>printing and typesetting industry.</p></div>
<div class="vstep right-align" style="top:1702px;left:170px"><h3>Start selling!</h3><p>Lorem Ipsum is simply dummy text of the<br>printing and typesetting industry.</p></div>
<div class="btn btn-orange" style="top:1813px;left:531px;width:137px;height:30px">Register As Vendor</div>

<!-- FAQ -->
<h2 class="section-title" style="top:1978px">Frequently asked questions</h2>
<div class="faq">
  <div class="faq-item"><span>It is a long established fact that a reader will be distracted</span><span class="sign">+</span></div>
  <div class="faq-item open"><div class="q"><span>Lorem Ipsum is simply dummy text</span><span class="sign">–</span></div>
    <p>Lorem Ipsum is simply dummy text of the printing and typesetting industry. Lorem Ipsum has been the industry's standard dummy text ever since the 1500s, when an unknown printer took a galley of type and scrambled it to make a type specimen book. It has survived not only five centuries, but also the</p></div>
  <div class="faq-item"><span>It is a long established fact that a reader will be distracted</span><span class="sign">+</span></div>
  <div class="faq-item"><span>Lorem Ipsum is simply dummy text</span><span class="sign">+</span></div>
  <div class="faq-item"><span>It is a long established fact that a reader will be distracted</span><span class="sign">+</span></div>
  <div class="faq-item"><span>Lorem Ipsum is simply dummy text</span><span class="sign">+</span></div>
  <div class="faq-item"><span>It is a long established fact that a reader will be distracted</span><span class="sign">+</span></div>
</div>

<!-- GET THE APP -->
<div class="band app-bg"></div>
<svg class="layer" style="top:2370px" width="1200" height="170" viewBox="0 2370 1200 170">
  <path d="M0,2370 H1200 V2412 C1080,2400 1000,2480 880,2490 C700,2505 640,2420 520,2450 C420,2475 360,2530 260,2525 C150,2520 80,2390 0,2378Z" fill="#ffffff" stroke="#ececec" stroke-width="4"/>
</svg>
<h2 class="abs app-title">Get the app</h2>
<div class="abs app-copy">It is a long established fact that a reader will be distracted by the readable content of a page when looking at its layout. The point of using lorem Ipsum is that it has.</div>
<div class="badge" style="top:2653px;left:200px"></div>
<div class="badge" style="top:2653px;left:312px"></div>
<div class="placeholder" role="img" aria-label="App start screen with a delivery rider over a city skyline" style="top:2500px;left:760px;width:230px;height:240px;background:linear-gradient(180deg,#f7a046,#f47c20 70%,#e06a18)"></div>

<!-- FOOTER -->
<div class="band footer-bg"></div>
<div class="abs brand" style="top:2812px;left:200px;font-size:22px"><span class="brand-dot" style="width:26px;height:26px"></span>dapurlaju</div>
<div class="abs contact" style="top:2852px;left:200px">
  <div class="call">Call: 123-456-7890</div>
  <div>info@dapurlaju.com</div>
  <div style="margin-top:18px;line-height:14px">Loremipsum workingfrom 123,<br>6004 lorem projects, info<br>work-12345</div>
</div>
<div class="abs foot-col" style="top:2818px;left:436px">
  <h4>Quick Links</h4>
  <a>Home</a><a>About Us</a><a>FAQ</a><a class="hl">Vendor Registration</a><a>Careers</a><a>Contact Us</a>
</div>
<div class="abs foot-col" style="top:2818px;left:612px">
  <h4>Learn More</h4>
  <a>Food Menu</a><a>Covid-19 Updates</a><a>Terms &amp; Conditions</a><a>Disclaimer</a><a>Privacy Policy</a>
</div>
<div class="abs select"><span class="flag"></span>Malaysia<span class="chev">&#8964;</span></div>
<div class="social" style="left:818px"></div>
<div class="social" style="left:850px;background:var(--orange)"></div>
<div class="social" style="left:882px"></div>
<div class="abs copyright">© 2021 <b style="font-weight:500">DapurLaju.com</b> All Rigth Reserved.</div>
<div class="badge" style="top:3005px;left:612px"></div>
<div class="badge" style="top:3005px;left:725px"></div>
<svg class="layer" style="top:3010px;left:990px" width="20" height="20" viewBox="0 0 20 20"><path d="M10,3 L17,17 L10,13 L3,17Z" fill="none" stroke="#f39c1f" stroke-width="1.5" stroke-linejoin="round"/></svg>

</body>
</html>
```